Business card por a urban DJ, up scale audience target

Need a sober design, modern, conservative colors but i can consider some options, y play rnb, hip hop, EDM and top40.

Business card for contact and personal info, double sided, use logo attrached please; im 42 so i need a card acording to my age an target audience.

Target Market(s)

Adult people, up scale audience

Industry/Entity Type

Music Download

Contact Information for Business Card

Cel (318) 5024471963 www.kelvarodun.com

Requirements
Must have
• open mind
Nice to have
• open mind
Should not have
• DJ

```html
<!DOCTYPE html>
<html lang="en">
<head>
<meta charset="UTF-8">
<title>Marcus Hale — Business Card</title>
<link href="https://fonts.googleapis.com/css2?family=Jost:wght@400;500;600&display=swap" rel="stylesheet">
<style>
  :root {
    --backdrop: #3a3d41;
    --card-light: #fbfbfb;
    --card-dark: #171717;
    --ink: #141414;
    --ink-muted: #8a8a8a;
    --ink-body: #333333;
    --paper: #ffffff;
  }
  * { margin: 0; padding: 0; box-sizing: border-box; }
  html, body {
    width: 1200px;
    height: 750px;
    overflow: hidden;
  }
  body {
    background: var(--backdrop);
    font-family: "Jost", sans-serif;
    position: relative;
  }
  .card {
    position: absolute;
    top: 228px;
    width: 461px;
    height: 262px;
  }
  .card--front {
    left: 124px;
    background: var(--card-light);
  }
  .card--back {
    left: 618px;
    background: var(--card-dark);
  }

  .front__accent {
    position: absolute;
    left: 0;
    top: 106px;
    width: 6px;
    height: 82px;
    background: var(--ink);
  }
  .front__name {
    position: absolute;
    left: 30px;
    top: 102px;
    font-size: 18px;
    font-weight: 500;
    color: var(--ink);
    letter-spacing: 0.2px;
  }
  .front__title {
    position: absolute;
    left: 30px;
    top: 124px;
    font-size: 13px;
    font-weight: 500;
    color: var(--ink-muted);
  }
  .front__contacts {
    position: absolute;
    left: 30px;
    top: 153px;
    list-style: none;
    font-size: 13px;
    color: var(--ink-body);
  }
  .front__contacts li {
    display: flex;
    align-items: center;
    gap: 6px;
    height: 18px;
  }
  .front__contacts svg { width: 11px; height: 11px; flex: none; }

  .brand {
    position: absolute;
    text-align: center;
    font-weight: 600;
    line-height: 1;
    white-space: nowrap;
  }
  .brand--front {
    left: 270px;
    top: 125px;
    width: 156px;
    font-size: 29px;
    letter-spacing: 1px;
    color: var(--ink);
  }
  .brand--back {
    left: 130px;
    top: 116px;
    width: 200px;
    font-size: 40px;
    letter-spacing: 1.5px;
    color: var(--paper);
  }

  .back__web {
    position: absolute;
    left: 0;
    width: 100%;
    top: 184px;
    text-align: center;
    font-size: 10px;
    font-weight: 600;
    letter-spacing: 2px;
    color: var(--paper);
  }
</style>
</head>
<body>
  <section class="card card--front">
    <span class="front__accent"></span>
    <h1 class="front__name">MARCUS HALE</h1>
    <p class="front__title">CEO/FOUNDER</p>
    <ul class="front__contacts">
      <li>
        <svg viewBox="0 0 11 11" aria-hidden="true"><rect x="2.5" y="0.5" width="6" height="10" rx="1" fill="none" stroke="#141414" stroke-width="1.2"/><rect x="4.5" y="8.2" width="2" height="1" fill="#141414"/></svg>
        (318) 5024471963
      </li>
      <li>
        <svg viewBox="0 0 11 11" aria-hidden="true"><circle cx="5.5" cy="5.5" r="5" fill="#141414"/><path d="M3 3.5 L5 4 L4.5 6 L6.5 7.5 L6 9.5 M7.5 2 L8 4 L9.5 4.5" fill="none" stroke="#fbfbfb" stroke-width="0.9"/></svg>
        www.kelvarodun.com
      </li>
    </ul>
    <p class="brand brand--front">KELVARO</p>
  </section>

  <section class="card card--back">
    <p class="brand brand--back">KELVARO</p>
    <p class="back__web">WWW.KELVARODUN.COM</p>
  </section>
</body>
</html>
```